Problem Solving Guide- PDF Template

We are looking for an editable PDF template design for our Epoxy Floor Coatings Problem Solving Guide.

Target Market(s)

This guide will be on our website and we will also email it to customers

Industry/Entity Type

Online Shopping

Colors
f78f20
ffffff
5c5c5c
000000

Requirements
Must have
• We are looking for a very modern and clean design. Each page of the guide will address a different issue. There will be 20-25 pages in total for the completed guide, however we just need a template that we can use to create each page so that they look the same. Each page must have our logo, a spot to add a photo of the issue being discussed. Then each page will have the following sections: DESCRIPTION,CAUSE,REPAIR,PREVENTION. At the bottom of each page we would like to direct people to our website for more information. I am attaching the current guide that we have. This shows the basic information that each page will have but as you can see it is old, outdated and anything but modern. As part of the design you can put the different parts of information in circles, squares, use arrows etc. to make it appealing. I am also attaching a copy of our color chart that appears on our website to give you an idea of some of the other graphic designs that we use. Our colors are Orange (please use the same orange as in our logo) grey, black and white. Our website is www.resinmarko.com. There is also a picture of "bubbles in epoxy"-this is an example of a picture we will show to address one issue.

```html
<!DOCTYPE html>
<html lang="en">
<head>
<meta charset="utf-8">
<title>Epoxy Floor Coatings – Problem Solving Guide</title>
<link href="https://fonts.googleapis.com/css2?family=Montserrat:wght@300;400;600;700;800&display=swap" rel="stylesheet">
<style>
  :root{
    --orange:#f78f20;
    --orange-deep:#ec6430;
    --grey:#5c5c5c;
    --grey-light:#e8e8e8;
    --black:#000000;
    --white:#ffffff;
  }
  *{margin:0;padding:0;box-sizing:border-box}
  html,body{width:848px;height:1200px;overflow:hidden;background:var(--white)}
  body{font-family:'Montserrat',Arial,sans-serif;color:var(--black)}
  .page{position:relative;width:848px;height:1200px;overflow:hidden;background:var(--white)}
  .abs{position:absolute}

  .header-band{left:0;top:0;width:848px;height:130px}
  .guide-title{right:52px;top:40px;text-align:right;color:var(--white);line-height:1.22}
  .guide-title .light{font-weight:300;font-size:24px;letter-spacing:-.4px}
  .guide-title .bold{font-weight:700;font-size:24px;letter-spacing:-.6px}

  .issue-title{left:52px;top:222px;font-size:31px;font-weight:800;letter-spacing:-.8px}

  .description{left:51px;top:293px;width:746px;height:233px}
  .description .strip{left:0;top:0;width:66px;height:233px;background:var(--orange);clip-path:polygon(0 0,100% 0,100% 100%,14px 100%,0 219px)}
  .description .body{left:66px;top:0;width:320px;height:233px;background:var(--orange-deep)}
  .description .photo{left:335px;top:0;width:411px;height:233px;background:linear-gradient(135deg,#9a9a9a,#858585 55%,#7a7a7a)}
  .description .notch{left:315px;top:100px;width:20px;height:32px;background:var(--orange-deep);clip-path:polygon(0 0,100% 50%,0 100%)}
  .section-head{font-weight:700;font-size:14.5px;letter-spacing:-.2px}
  .description h2{position:absolute;left:19px;top:22px;color:var(--white)}
  .description p{position:absolute;left:19px;top:54px;width:226px;color:var(--white);font-weight:600;font-size:12.2px;line-height:17px}
  .info-icon{left:12px;top:21px}

  .cause,.repair{top:574px;width:240px}
  .cause{left:159px}.repair{left:557px}
  .col-text{margin-top:18px;font-size:12.4px;line-height:17px;color:#1a1a1a}
  .cause-illus{left:54px;top:576px;width:92px;height:106px;background:linear-gradient(180deg,#f5b82e,#f39a2a);border-radius:6px}
  .repair-illus{left:436px;top:576px;width:106px;height:106px;background:linear-gradient(180deg,#e7734a,#f3c9a3);border-radius:50%}

  .prevention{left:51px;top:810px;width:605px;height:102px}
  .prevention .label-box{left:0;top:0;width:133px;height:102px;background:var(--orange-deep);clip-path:polygon(0 0,100% 0,100% 100%,14px 100%,0 88px)}
  .prevention .text-box{left:133px;top:0;width:472px;height:102px;background:var(--orange)}
  .prevention h2{position:absolute;left:20px;top:20px;color:var(--white);font-size:15px}
  .prevention p{position:absolute;left:16px;top:17px;width:436px;color:var(--white);font-weight:600;font-size:12.2px;line-height:17px}
  .roller-illus{left:654px;top:788px;width:143px;height:140px;background:linear-gradient(135deg,#fcd03d,#f28c2a 70%,#506770);border-radius:10px}

  .batch-illus{left:64px;top:948px;width:176px;height:116px;background:linear-gradient(135deg,#f5a04a,#dfe6ee 60%,#f39a2a);border-radius:10px}
  .batch{left:283px;top:963px;width:512px}
  .batch .col-text{margin-top:22px}

  .footer-band{left:0;top:1130px;width:848px;height:70px}
  .footer-brand{right:52px;top:1112px;text-align:right}
  .brand-name{font-size:26px;font-weight:700;color:var(--grey);letter-spacing:-.5px;line-height:1}
  .brand-tag{font-size:9.5px;color:var(--grey);margin-top:5px;font-weight:400}
</style>
</head>
<body>
<main class="page">

  <svg class="abs header-band" viewBox="0 0 848 130" aria-hidden="true">
    <rect x="0" y="0" width="848" height="64" fill="var(--orange)"/>
    <path d="M0 64 H455 Q470 64 476 76 L492 112 Q498 124 512 124 H848 V64 Z" fill="var(--orange)"/>
  </svg>
  <div class="abs guide-title">
    <div class="light">Epoxy Floor Coatings</div>
    <div class="bold">Problem Solving Guide</div>
  </div>

  <h1 class="abs issue-title">COLOR DIFFERENTIAL</h1>

  <section class="abs description">
    <div class="abs strip">
      <svg class="abs info-icon" width="36" height="40" viewBox="0 0 36 40" aria-hidden="true">
        <circle cx="16" cy="16" r="14" fill="#e3322b"/>
        <rect x="14.5" y="14" width="3" height="9" fill="#fff"/>
        <circle cx="16" cy="10" r="2" fill="#fff"/>
      </svg>
    </div>
    <div class="abs body">
      <h2 class="section-head">DESCRIPTION:</h2>
      <p>Edit quam qui blam aliqui occuptin consequ atusciam, sequi optati nones eat enditatur sequid quunto iliae nem alit, nemolor estiis aut</p>
    </div>
    <div class="abs photo" role="img" aria-label="Photo of the floor issue: bubbles in a grey epoxy coating"></div>
    <div class="abs notch" aria-hidden="true"></div>
  </section>

  <div class="abs cause-illus" role="img" aria-label="Illustration of a yellow wet-floor warning sign"></div>
  <section class="abs cause">
    <h2 class="section-head">CAUSE:</h2>
    <p class="col-text">Edit quam qui blam aliqui occuptin consequ atusciam, sequi optati nones eat enditatur sequid quunto iliae nem alit, nemolor estiis aut Ad quunti ipsam, nem ipicien dicimin ciation sequoditia dia vendae volorem restiur? Quia nullab id quidunt ducid molendi pidebit velitat emoluptis escidio</p>
  </section>

  <div class="abs repair-illus" role="img" aria-label="Illustration of a support agent with a repair tool bubble"></div>
  <section class="abs repair">
    <h2 class="section-head">REPAIR:</h2>
    <p class="col-text">Edit quam qui blam aliqui occuptin consequ atusciam, sequi optati nones eat enditatur sequid quunto iliae nem alit, nemolor estiis aut Ad quunti ipsam, nem ipicien dicimin ciation sequoditia dia vendae volorem restiur? Quia nullab id quidunt ducid molendi pidebit velitat emoluptis escidio</p>
  </section>

  <section class="abs prevention">
    <div class="abs label-box"><h2 class="section-head">PREVENTION:</h2></div>
    <div class="abs text-box">
      <p>Edit quam qui blam aliqui occuptin consequ atusciam, sequi optati nones eat enditatur sequid quunto iliae nem alit, nemolor estiis aut Am que preprempe cum earuntium dipis ulpa parchici nobist laccatur? Uciunt id undi officiae im iduntur solum faccus doles</p>
    </div>
  </section>
  <div class="abs roller-illus" role="img" aria-label="Illustration of a paint roller with sparkles"></div>

  <div class="abs batch-illus" role="img" aria-label="Illustration of numbers under a magnifying glass"></div>
  <section class="abs batch">
    <h2 class="section-head">DIFFERENT BATCH NUMBERS:</h2>
    <p class="col-text">Edit quam qui blam aliqui occuptin consequ atusciam, sequi optati nones eat enditatur sequid quunto iliae nem alit, nemolor estiis aut Ad quunti ipsam, nem ipicien dicimin ciation sequoditia dia vendae</p>
  </section>

  <svg class="abs footer-band" viewBox="0 0 848 70" aria-hidden="true">
    <path d="M0 2 H232 Q246 2 252 14 L262 34 Q266 42 280 42 H848 V70 H0 Z" fill="var(--grey-light)"/>
  </svg>
  <div class="abs footer-brand">
    <div class="brand-name">Resinmarko</div>
    <div class="brand-tag">Floor coatings and much more.</div>
  </div>

</main>
</body>
</html>
```